Emergency Vehicle Installer and Security Firm Needs a Business Card

Our company "Corvalta" need a business card for our Emergency Vehicle Equipment Installation and Infrastructure Security Business. We are contract designers, manufacturers and installers for Emergency Vehicle Fleets. This includes installation of Emergency Lights, Sirens, Vehicle Graphics and Radio Communications. We also supply this products to an international market. We also do consultant, and installation of high level security access, alarm and surveillance equipment for medium to large size businesses.

The design should represent a level of trust in our professionalism and expertise. It should visually display our ongoing relationship with the emergency services, but not overtake our commitment to high level security options.

Target Market(s)

Emergency Services and Businesses requiring high level security

Industry/Entity Type

Business

Contact Information for Business Card

*note complete details will be given to the winning designer for revising. The name "Mark Pelling will be used to fill in name".

Mark Pelling
Managing Director
Corvalta NZ Limited
Phone: +64 027 846 20193
Email: mark.pelling@corvalta-example.co.nz

Requirements
Must have
• Card must be in black. Using our logo on the top as supplied. Designers should try having the reverse side as a blurred image of police lights (red and blue) with our logo in greyscale in the centre (this is not particularly a requirement, but feel free to play around with this option).
Nice to have
• A card design that looks good when spot UV printed. A clean compact and graphic design. A grey scale feel on the front (excluding logo, but you can play around with that idea). Rounded smooth text.
Should not have
• Will update this section as designs come through - feel free to submit what you feel would look good.

```html
<!DOCTYPE html>
<html lang="en">
<head>
<meta charset="utf-8">
<title>Corvalta Business Card</title>
<link rel="stylesheet" href="https://fonts.googleapis.com/css2?family=Arimo:wght@400;700&display=swap">
<style>
  :root {
    --backdrop: #2b2b2b;
    --card-black: #0b0b0b;
    --card-sheen: #1a1a1a;
    --text-light: #e6e6e6;
    --accent-red: #e0282c;
    --rule-grey: #8a8a8a;
  }
  * { margin: 0; padding: 0; box-sizing: border-box; }
  html, body {
    width: 1200px;
    height: 950px;
    overflow: hidden;
    background: var(--backdrop);
    font-family: "Arimo", Arial, sans-serif;
  }
  .sheet {
    position: relative;
    width: 1200px;
    height: 950px;
  }
  .card {
    position: absolute;
    left: 250px;
    width: 700px;
    height: 400px;
    background: linear-gradient(135deg, var(--card-sheen) 0%, var(--card-black) 55%);
    box-shadow: 0 12px 30px rgba(0, 0, 0, 0.6);
  }
  .card--front { top: 60px; }
  .card--back { top: 490px; }

  .brand {
    position: absolute;
    top: 50%;
    left: 50%;
    transform: translate(-50%, -50%);
    display: flex;
    align-items: center;
    gap: 18px;
  }
  .brand__dot {
    width: 26px;
    height: 26px;
    border-radius: 50%;
    background: var(--accent-red);
  }
  .brand__name {
    font-weight: 700;
    font-size: 64px;
    letter-spacing: 2px;
    color: var(--text-light);
  }

  .contact {
    position: absolute;
    top: 120px;
    left: 0;
    right: 0;
    text-align: center;
    color: var(--text-light);
    font-size: 17px;
    line-height: 1.55;
  }
  .contact__name {
    color: var(--accent-red);
    font-size: 24px;
    line-height: 1.3;
  }
  .contact__role { font-size: 19px; margin-bottom: 14px; }
  .contact__rule {
    position: absolute;
    left: 330px;
    top: 300px;
    width: 300px;
    height: 1px;
    background: linear-gradient(90deg, transparent, var(--rule-grey), transparent);
  }
</style>
</head>
<body>
<main class="sheet">
  <section class="card card--front" aria-label="Card front">
    <div class="brand">
      <span class="brand__dot"></span>
      <span class="brand__name">CORVALTA</span>
    </div>
  </section>

  <section class="card card--back" aria-label="Card back">
    <div class="contact">
      <p class="contact__name">Mark Pelling</p>
      <p class="contact__role">Managing Director</p>
      <p class="contact__line">+64 027 846 20193 | mark.pelling@corvalta-example.co.nz</p>
      <p class="contact__company">Corvalta NZ Limited</p>
    </div>
    <div class="contact__rule"></div>
  </section>
</main>
</body>
</html>
```